Business Card Design Project

New business card design front and back for IT company that does network support and web design.
Calloway IT
Derek Calloway
Managing Director
PO Box 582 Tarrowby VIC 3267
derek@callowayit.example
www.callowayit.example

Industry/Entity Type

Business

```html
<!DOCTYPE html>
<html lang="en">
<head>
<meta charset="utf-8">
<title>Calloway IT – Business Card</title>
<link href="https://fonts.googleapis.com/css2?family=Questrial&display=swap" rel="stylesheet">
<style>
  :root {
    --brand-yellow: #fec70f;
    --brand-yellow-light: #ffdc5a;
    --ink-black: #000000;
    --panel-dark: #141414;
    --panel-darker: #0b0b0b;
    --paper-white: #ffffff;
  }
  html, body {
    margin: 0;
    padding: 0;
    width: 1200px;
    height: 741px;
    overflow: hidden;
    background: var(--ink-black);
  }
  .card {
    position: relative;
    width: 1200px;
    height: 741px;
    overflow: hidden;
    font-family: "Questrial", "Century Gothic", sans-serif;
  }
  .card-front {
    position: absolute;
    left: 0;
    top: 0;
    width: 739px;
    height: 741px;
    background: var(--brand-yellow);
  }
  .network-illustration {
    position: absolute;
    left: 262px;
    top: 28px;
    width: 428px;
    height: 296px;
    border-radius: 40px 40px 140px 140px;
    background: radial-gradient(ellipse at 50% 40%, var(--brand-yellow-light) 0%, rgba(255, 220, 90, 0.45) 55%, rgba(254, 199, 15, 0) 100%);
    opacity: 0.8;
  }
  .divider-rule {
    position: absolute;
    left: 0;
    top: 234px;
    width: 671px;
    height: 15px;
    background: var(--ink-black);
  }
  .holder-name {
    position: absolute;
    left: 63px;
    top: 294px;
    margin: 0;
    font-size: 77px;
    font-weight: 400;
    line-height: 1;
    color: var(--paper-white);
    letter-spacing: 0.5px;
    white-space: nowrap;
  }
  .holder-details {
    position: absolute;
    left: 65px;
    top: 427px;
    margin: 0;
    font-size: 56px;
    line-height: 68px;
    color: var(--ink-black);
    font-style: normal;
    white-space: nowrap;
  }
  .holder-details span { display: block; }
  .card-back {
    position: absolute;
    left: 739px;
    top: 0;
    width: 461px;
    height: 741px;
    background: linear-gradient(160deg, var(--panel-dark) 0%, var(--panel-darker) 100%);
  }
  .back-band {
    position: absolute;
    left: 0;
    top: 311px;
    width: 100%;
    height: 127px;
    background: var(--ink-black);
  }
  .contact-email {
    position: absolute;
    left: 14px;
    top: 653px;
    display: flex;
    align-items: center;
    gap: 9px;
    font-size: 31px;
    color: var(--brand-yellow);
    white-space: nowrap;
  }
  .mail-icon { width: 43px; height: 29px; flex: none; }
</style>
</head>
<body>
  <div class="card">
    <section class="card-front">
      <div class="network-illustration" role="img" aria-label="Faint illustration of networked computer monitors"></div>
      <div class="divider-rule"></div>
      <h1 class="holder-name">Derek Calloway</h1>
      <address class="holder-details">
        <span>Managing Director</span>
        <span>PO Box 582 Tarrowby</span>
        <span>VIC 3267</span>
        <span>0491 570 006</span>
      </address>
    </section>
    <section class="card-back">
      <div class="back-band"></div>
      <div class="contact-email">
        <svg class="mail-icon" viewBox="0 0 43 29" aria-hidden="true">
          <rect x="1" y="1" width="41" height="27" fill="#fde7a0" stroke="#d9a300" stroke-width="2"/>
          <path d="M1 1 L21.5 17 L42 1" fill="none" stroke="#d9a300" stroke-width="2"/>
          <path d="M1 28 L16 13 M42 28 L27 13" fill="none" stroke="#d9a300" stroke-width="1.5"/>
        </svg>
        <span>derek@callowayit.example</span>
      </div>
    </section>
  </div>
</body>
</html>
```